Tumbleweed Photography needs a promotional flyer to bring in new studio shoots.

I need a flyer which will create interest and leads for my business. The idea behind the driection i want to go is a Free Photoshoot, specifically aimed at families, i want to put customers in control of what they want to purchase, they choose the prints they would like to buy and we can frame them also. I would designs which feature happy, smiling, laughing people/families, without being too cute. The final design should convey fun and professionalism.

The address is 418 Morrow Parade, Bayswater, WA6053, website is www.tumbleweedphotography.com.au, contact numbers are 0492 317 658 or 08 6257 1894, email is darrenh@tumbleweedphotography.com.au

I would like some focus on "Free Photoshoot", This is key to the message i want to get out. Maybe, "Free Photoshoot, we put you in control!" THe idea behind the free photoshoot is families pay for what they want after the photoshoot is done, the flyer doesn't need to explain the whole process, just highlight the free photoshoot, the website can explain the rest. Thanks Darren

```html
<!DOCTYPE html>
<html lang="en">
<head>
<meta charset="utf-8">
<title>Tumbleweed Photography – Flyer</title>
<link href="https://fonts.googleapis.com/css2?family=Mulish:wght@400;700;800&display=swap" rel="stylesheet">
<style>
  :root {
    --page-bg: #e9e7e3;
    --paper: #f4f4f4;
    --paper-edge: #ffffff;
    --ink: #2e2e2e;
    --ink-soft: #555555;
    --band: #3a3a3a;
    --band-text: #ffffff;
    --photo-sky: #9fa8b3;
    --photo-warm: #c9b9a6;
    --photo-green: #8fa36d;
    --studio-light: #e6e3df;
    --studio-mid: #c7c1ba;
    --ring: #ffffff;
  }
  * { box-sizing: border-box; margin: 0; padding: 0; }
  html, body { width: 1200px; height: 1000px; overflow: hidden; }
  body {
    background: var(--page-bg);
    font-family: "Mulish", sans-serif;
    color: var(--ink);
    display: flex; align-items: center; justify-content: center;
  }
  .flyer {
    width: 660px; height: 940px;
    background: radial-gradient(ellipse at 50% 55%, var(--paper-edge) 0%, var(--paper) 70%, #e4e4e4 100%);
    box-shadow: 0 6px 24px rgba(0,0,0,.18);
    padding: 28px 34px 28px;
    display: flex; flex-direction: column;
  }
  .header { display: flex; gap: 28px; align-items: flex-start; margin-bottom: 12px; }
  .brand { width: 220px; display: flex; align-items: center; gap: 10px; padding-top: 22px; }
  .brand-mark { width: 22px; height: 22px; background: var(--ink); flex: none; }
  .brand-name { font-size: 21px; font-weight: 700; color: var(--ink); line-height: 1.1; }
  .intro { flex: 1; font-size: 11px; line-height: 1.5; color: var(--ink-soft); }
  .intro p + p { margin-top: 5px; }
  .intro strong { color: var(--ink); }
  .hero {
    height: 270px; border-radius: 2px; flex: none;
    background: linear-gradient(160deg, var(--photo-sky) 0%, #b8bfc8 45%, var(--photo-warm) 70%, var(--photo-green) 100%);
  }
  .tagline {
    background: var(--band); color: var(--band-text);
    font-size: 24px; font-weight: 800; text-align: center;
    padding: 10px 0; margin-top: -20px; margin-right: -34px;
    position: relative;
  }
  .framing { font-size: 12.5px; line-height: 1.5; text-align: center; color: var(--ink-soft); margin: 12px 20px 0; }
  .framing strong { color: var(--ink); }
  .free-shoot { display: block; font-size: 17px; font-weight: 800; color: var(--ink); margin-bottom: 4px; }
  .gallery { display: flex; justify-content: space-between; padding: 12px 18px 0; }
  .gallery-shot {
    width: 150px; height: 150px; border-radius: 50%;
    border: 6px solid var(--ring);
    box-shadow: 0 2px 8px rgba(0,0,0,.2);
    background: radial-gradient(circle at 50% 45%, var(--studio-light) 0%, var(--studio-mid) 100%);
  }
  .gallery-shot:nth-child(2) { margin-top: 30px; }
  .gallery-shot:nth-child(3) { margin-top: 60px; }
  .frames { font-size: 12.5px; line-height: 1.5; text-align: center; color: var(--ink-soft); margin: 10px 10px 0; }
  .frames strong { color: var(--ink); }
  .contact {
    margin-top: auto;
    background: var(--band); color: var(--band-text);
    display: flex; align-items: center; gap: 16px;
    padding: 14px 18px; font-size: 12px; line-height: 1.5;
  }
  .contact-icon { width: 32px; height: 32px; flex: none; }
  .contact-block { flex: none; white-space: nowrap; padding-right: 16px; border-right: 1px solid rgba(255,255,255,.5); }
  .contact-block:last-child { border-right: none; padding-right: 0; }
  .contact strong { font-weight: 700; }
</style>
</head>
<body>
  <main class="flyer">
    <header class="header">
      <div class="brand">
        <span class="brand-mark"></span>
        <span class="brand-name">Tumbleweed Photography</span>
      </div>
      <div class="intro">
        <p><strong>Tumbleweed Photography</strong> was created to offer Perth a fun, relaxed, yet professional and current business specialising in family portraits and studio photography.</p>
        <p>From family photography to portfolio head shots, we can assist and work with you to preserve today's moments for tomorrow's treasured memories.</p>
      </div>
    </header>

    <div class="hero" role="img" aria-label="Smiling family of four sitting together outside a house"></div>

    <h1 class="tagline">Photography and Framing made easy!</h1>

    <p class="framing"><span class="free-shoot">Free Photoshoot, we put you in control!</span>Tumbleweed Photography also offers a hand-crafted framing service, and if you choose to avail of this we will print your chosen images for <strong>free!</strong></p>

    <div class="gallery">
      <div class="gallery-shot" role="img" aria-label="Family portrait in the studio"></div>
      <div class="gallery-shot" role="img" aria-label="Baby sitting on a white studio backdrop"></div>
      <div class="gallery-shot" role="img" aria-label="Parents holding their baby in the studio"></div>
    </div>

    <p class="frames">We offer a comprehensive selection of frames to choose from which are mounted in our studio.<br><strong>Visit our website and see the "Framing" tab to learn more.</strong></p>

    <footer class="contact">
      <svg class="contact-icon" viewBox="0 0 34 34" aria-hidden="true">
        <circle cx="17" cy="17" r="15" fill="none" stroke="#fff" stroke-width="2"/>
        <path d="M12 10c1-1 2.5-1 3 .2l1.2 2.8c.3.8 0 1.5-.6 2l-1 .8c.8 1.8 2 3 3.7 3.8l.8-1c.5-.6 1.3-.8 2-.5l2.8 1.2c1.1.5 1.2 2 .2 3l-1 1c-1.5 1.4-5 .5-8.2-2.7S10.4 12.5 12 10z" fill="#fff"/>
      </svg>
      <div class="contact-block">0492 317 658<br>08 6257 1894</div>
      <div class="contact-block"><strong>418 Morrow Parade,</strong><br>Bayswater, WA6053</div>
      <div class="contact-block">www.tumbleweedphotography.com.au<br>darrenh@tumbleweedphotography.com.au</div>
    </footer>
  </main>
</body>
</html>
```